Label design

Description
I want you to design a label for a skin care product line. I’ve provide the picture of the jar we are using along with the logo. Please note that the logo is available in different colors as well. (See attached) I would like the label to be very clean and straight to the point. Here is some info that I would like to see on the label:
240G
Net wt 8.0z

The content of the jar can be refer to as:

Body cream
Crème de corps
Body butter
Fade cream
Skin tone cream
Lotion pour le corps
Clarifying Body cream
Lightening Cream

The content is also made an exotic component that: “Extraits de noisette de palmiers” meaning nuts extract.

The brand NAME is: Mibaru
The tag line is: Be yourself, love yourself

Industry/Entity Type

Skin Care Product

```html
<!DOCTYPE html>
<html lang="fr">
<head>
<meta charset="utf-8">
<title>Mibaru – Body cream label</title>
<link href="https://fonts.googleapis.com/css2?family=Quicksand:wght@400;500&family=Kalam:wght@300&display=swap" rel="stylesheet">
<style>
  :root {
    --backdrop: #ececec;
    --label-white: #fbfbf9;
    --label-rule: #b9b9b9;
    --ink: #3e3e3e;
    --ink-soft: #555555;
    --brand-gold: #c08a34;
    --gold-dark: #8e5b1d;
    --gold-mid: #c9922e;
    --gold-light: #f3cb62;
    --band-text: #ffffff;
  }
  * { margin: 0; padding: 0; box-sizing: border-box; }
  html, body {
    width: 1200px;
    height: 1000px;
    overflow: hidden;
    background: var(--backdrop);
  }
  .canvas {
    position: relative;
    width: 1200px;
    height: 1000px;
  }
  .label {
    position: absolute;
    left: 100px;
    top: 190px;
    width: 1000px;
    height: 620px;
    background: var(--label-white);
    border: 2px solid var(--label-rule);
    font-family: "Quicksand", sans-serif;
    color: var(--ink);
  }
  .ingredient-note {
    position: absolute;
    left: 58px;
    top: 88px;
    font-size: 34px;
    line-height: 1.3;
    color: var(--ink-soft);
    font-weight: 500;
  }
  .tagline {
    position: absolute;
    right: 60px;
    top: 80px;
    font-family: "Kalam", cursive;
    font-weight: 300;
    font-size: 42px;
    line-height: 1.25;
    color: var(--ink-soft);
  }
  .brand {
    position: absolute;
    left: 0;
    right: 0;
    top: 250px;
    display: flex;
    justify-content: center;
    align-items: center;
    gap: 18px;
  }
  .brand-dot {
    width: 22px;
    height: 22px;
    border-radius: 50%;
    background: var(--brand-gold);
  }
  .brand-name {
    font-size: 84px;
    font-weight: 400;
    color: var(--brand-gold);
    line-height: 1;
  }
  .product-band {
    position: absolute;
    left: 0;
    right: 0;
    top: 388px;
    height: 92px;
    background: linear-gradient(90deg,
      var(--gold-dark) 0%,
      var(--gold-mid) 18%,
      var(--gold-light) 42%,
      var(--gold-mid) 62%,
      var(--gold-light) 80%,
      var(--gold-dark) 100%);
    display: flex;
    align-items: center;
    justify-content: center;
  }
  .product-name {
    color: var(--band-text);
    font-size: 62px;
    font-weight: 400;
    line-height: 1;
  }
  .product-name-fr {
    position: absolute;
    left: 0;
    right: 0;
    top: 502px;
    text-align: center;
    font-size: 50px;
    font-weight: 400;
    color: var(--ink);
  }
  .net-weight {
    position: absolute;
    right: 36px;
    top: 500px;
    text-align: right;
    font-size: 20px;
    line-height: 1.2;
    color: var(--ink-soft);
  }
</style>
</head>
<body>
  <main class="canvas">
    <section class="label" aria-label="Mibaru body cream label">
      <p class="ingredient-note">Extraits de<br>noisette<br>de palmiers</p>
      <p class="tagline">Be yourself,<br>love yourself</p>
      <div class="brand">
        <span class="brand-dot" aria-hidden="true"></span>
        <span class="brand-name">Mibaru</span>
      </div>
      <div class="product-band">
        <h1 class="product-name">Body cream</h1>
      </div>
      <p class="product-name-fr">Crème de corps</p>
      <p class="net-weight">240G<br>Net wt 8.0z</p>
    </section>
  </main>
</body>
</html>
```